Business Card Design for company

We want new business cards. We'd like something different-- yet still highly professional. Our tagline is Providing leadership, delivering success. Stock photos are ok, as long as they are relevant and look upscale.

Target Market(s)

Architecture/Business Management Consulting/Engineering Consulting

Contact Information for Business Card

dark gray background with pops of blue might be good, but you tell me. You're the designers. Rounded corners might be nice, but again, you tell me.

Font styles to use
Serif
Sans Serif

Colors
3276b5
5c5c5c
9d9d9d
fbfbfb

Requirements
Nice to have
• Something different, but still very professional.

```html
<!DOCTYPE html>
<html lang="en">
<head>
<meta charset="utf-8">
<title>Halden Partners Business Card</title>
<link href="https://fonts.googleapis.com/css2?family=Lato:wght@400;700;900&display=swap" rel="stylesheet">
<style>
  :root {
    --stage: #2a2929;
    --card-dark: #1d1d1d;
    --map-tone: #2b2b2b;
    --card-light: #fbfbfb;
    --blue: #3276b5;
    --gray: #5c5c5c;
    --gray-light: #9d9d9d;
    --ink: #2b2b2b;
  }
  * { margin: 0; padding: 0; box-sizing: border-box; }
  html, body { width: 1200px; height: 895px; overflow: hidden; }
  body {
    background: var(--stage);
    font-family: "Lato", sans-serif;
    position: relative;
  }
  .card {
    position: absolute;
    width: 540px;
    height: 309px;
    border-radius: 14px;
    overflow: hidden;
  }
  .card-back { left: 40px; top: 293px; background: var(--card-dark); }
  .card-front { left: 620px; top: 293px; background: var(--card-light); border-radius: 4px; }

  .world-map {
    position: absolute;
    left: 60px; top: 30px;
    width: 420px; height: 200px;
    border-radius: 40px;
    background: radial-gradient(ellipse at center, var(--map-tone) 0%, rgba(43,43,43,0.4) 60%, rgba(29,29,29,0) 100%);
  }
  .back-brand {
    position: absolute;
    left: 56px; top: 190px;
    color: var(--gray-light);
    font-weight: 900;
    font-size: 30px;
    letter-spacing: 2px;
    line-height: 1.05;
    text-transform: uppercase;
  }

  .front-brand {
    position: absolute;
    left: 340px; top: 66px;
    color: var(--blue);
    font-weight: 900;
    font-size: 25px;
    letter-spacing: 1px;
    line-height: 1.1;
    text-transform: uppercase;
  }

  .contact-block {
    position: absolute;
    right: 230px; top: 46px;
    text-align: right;
    color: var(--ink);
  }
  .group {
    position: relative;
    padding-right: 14px;
    margin-bottom: 12px;
  }
  .group::after {
    content: "";
    position: absolute;
    right: 0; top: 2px; bottom: 2px;
    width: 1px;
    background: var(--gray);
  }
  .person-name { color: var(--blue); font-weight: 900; font-size: 21px; letter-spacing: 1px; line-height: 1.05; }
  .person-role { font-size: 12px; line-height: 1.3; }
  .address, .contacts { font-size: 11.5px; line-height: 1.45; }
  .contacts li { list-style: none; display: flex; justify-content: flex-end; align-items: center; gap: 6px; }
  .contacts svg { width: 10px; height: 10px; fill: var(--blue); flex: none; }

  .swoosh { position: absolute; left: 0; bottom: 0; width: 540px; height: 309px; }
</style>
</head>
<body>
  <section class="card card-back">
    <div class="world-map" role="img" aria-label="Faint world map across the card back"></div>
    <div class="back-brand">Halden<br>Partners</div>
  </section>

  <section class="card card-front">
    <svg class="swoosh" viewBox="0 0 540 309" aria-hidden="true">
      <path d="M0,266 C170,236 380,214 540,148 L540,162 C380,232 170,258 0,284 Z" fill="var(--gray)"/>
      <path d="M0,290 C170,264 380,242 540,170 L540,309 L0,309 Z" fill="var(--blue)"/>
    </svg>

    <div class="front-brand">Halden<br>Partners</div>

    <div class="contact-block">
      <div class="group">
        <div class="person-name">EVAN MARLOW</div>
        <div class="person-role">Director</div>
      </div>
      <div class="group address">
        <div>48 Westbrook Avenue</div>
        <div>Fairhaven, OR 97310</div>
      </div>
      <ul class="group contacts">
        <li>(503) 555-0142
          <svg viewBox="0 0 10 10"><path d="M2,0 L4,2 L3,3.5 C4,5 5,6 6.5,7 L8,6 L10,8 L8.5,10 C4,9 1,6 0,1.5 Z"/></svg></li>
        <li>hello@haldenpartners.com
          <svg viewBox="0 0 10 10"><path d="M0,2 L10,2 L10,8 L0,8 Z M0,2 L5,6 L10,2" stroke="#fbfbfb" stroke-width="0.8"/></svg></li>
        <li>www.haldenpartners.com
          <svg viewBox="0 0 10 10"><circle cx="5" cy="5" r="5"/><path d="M0,5 H10 M5,0 V10" stroke="#fbfbfb" stroke-width="0.7"/></svg></li>
      </ul>
    </div>
  </section>
</body>
</html>
```